依頼詳細
商品名:パームシュガー(ベトナム産)
容量:500g
デザイン:箱
添付している写真ファイル「包装」のように直径3.5cmの丸く固めたパームシュガーを数十個透明パックに入れて真空にして、箱に入れます。

サイズや文言などはPPTに記載しております。ベトナムでの販売が中心なので、日本語と英語、ベトナム語表記がありますが、英語とベトナム語は添付ファイル内にある文章をコピペしていただくだけです。

■裏面のデザインはほぼ不要

デザインのメインは表面と場合によって側面ちょっと。裏面は成分表や会社情報などが主なので、デザインはほぼなしで構いません。※文章はコピペ。

■イラスト&写真に関しまして

写真かイラストを入れていただきたいです。写真は法律で問題ないものをご使用くださいませ。弊社の方で持っている写真も添付します。

■ロゴに関しまして

弊社は現地では最近ネットなどで注目されているブランドです。できれば、ほどよくロゴを目立つようにしてください。

■デザインカラー

ロゴが水色(パステルカラー)なので、それに合わせた水色か、浅いピンクが希望です。

■納品形態
PNG、AI(アウトライン前と後をください)
■著作権
納品いただいた時点で弊社にわたるものとさせていただきます。

記載項目
サイズ:横11cm×高さ18.3cm×奥行2.6cm
詳細はPPT参照くださいませ。
希望イメージ
シンプル 複雑
単色 カラフル
暗い 明るい
日常 高級
遊び心 厳粛
未来的 伝統的
女性的 男性的
希望する色
赤系、水色系
納品ファイル
• イラストレーター形式 (.ai)
• PNG形式 (.png)
補足説明
この手のコンペなどは弊社は慣れておりませんので、ご質問ございましたらお気軽にご連絡ください。
依頼公開後の追記内容
ご提出いただいているデザイナーの方には大変申し訳ございませんが、案件が少ないため、一週間だけ延長させていただきます。
■ 選んだ理由

社内会議で慎重に選んだ結果、過半数でtavrin様に支持が集まりました。南国感、高級感、ギフト感とどれをとっても申し分ないデザインかと存じます。こちらの意図をしっかりと汲んでくれたと実感できるデザインです。

■ 提案者全員のお礼・コメント

この度は多数のご提案誠にありがとうございます。どれも非常に優れたデザインでした。また定期的にデザイン提案のご依頼をさせていただきますので、何卒よろしくお願い申し上げます。

```html
<!DOCTYPE html>
<html lang="ja">
<head>
<meta charset="utf-8">
<title>Palm Sugar Box Front</title>
<link href="https://fonts.googleapis.com/css2?family=Parisienne&family=Cormorant+Garamond:wght@500;600&family=Noto+Serif+JP:wght@500&display=swap" rel="stylesheet">
<style>
  :root{
    --paper:#ffffff;
    --aqua-light:#d6f1f1;
    --aqua-mid:#8fd4d9;
    --aqua-deep:#4fb1bd;
    --teal-veil:rgba(34,120,135,0.55);
    --cocoa:#4a3124;
    --ink:#2e3a3c;
    --script:#3b2a22;
    --white:#ffffff;
    --logo:#5cb9d4;
  }
  *{margin:0;padding:0;box-sizing:border-box}
  html,body{width:783px;height:1200px;overflow:hidden;background:var(--paper)}
  .box-front{position:relative;width:783px;height:1200px;background:var(--paper)}
  .panel{
    position:absolute;left:26px;top:21px;width:739px;height:1159px;
    background:
      radial-gradient(ellipse at 80% 20%, rgba(255,255,255,0.55), transparent 55%),
      linear-gradient(160deg,var(--aqua-light) 0%,var(--aqua-mid) 45%,var(--aqua-deep) 100%);
    overflow:hidden;
  }
  .name-band{
    position:absolute;left:0;top:157px;width:370px;height:62px;
    background:var(--cocoa);color:var(--white);
    font-family:"Noto Serif JP",serif;font-size:19px;letter-spacing:2px;
    display:flex;align-items:center;padding-left:34px;
  }
  .brand{
    position:absolute;right:28px;top:104px;
    display:flex;align-items:center;gap:10px;
    font-family:"Cormorant Garamond",serif;font-weight:600;font-size:30px;
    color:var(--logo);letter-spacing:2px;
  }
  .brand-dot{width:22px;height:22px;border-radius:50%;background:var(--logo)}
  .title{
    position:absolute;font-family:"Parisienne",cursive;color:var(--script);line-height:1;
  }
  .title-palm{left:92px;top:238px;font-size:150px}
  .title-sugar{left:282px;top:322px;font-size:150px}
  .veil{position:absolute;left:261px;top:397px;width:300px;height:274px;background:var(--teal-veil)}
  .product-photo{
    position:absolute;left:78px;top:436px;width:248px;height:313px;
    background:radial-gradient(circle at 40% 40%,#d9a66d,#9b6a3c 70%,#6e4624);
  }
  .story-en{
    position:absolute;left:338px;top:500px;width:370px;
    font-family:"Cormorant Garamond",serif;font-size:17px;line-height:1.75;color:var(--white);
  }
  .story-jp{
    position:absolute;left:162px;top:778px;
    font-family:"Noto Serif JP",serif;font-size:15px;line-height:2;color:var(--ink);
  }
  .palm-photo{
    position:absolute;left:222px;top:860px;width:457px;height:276px;
    background:linear-gradient(180deg,rgba(255,255,255,0) 0%,rgba(120,170,120,0.35) 55%,rgba(60,90,60,0.65) 100%);
  }
</style>
</head>
<body>
<div class="box-front">
  <div class="panel">
    <div class="name-band">パームシュガー</div>
    <div class="brand"><span class="brand-dot"></span>NAMIRA</div>
    <div class="title title-palm">Palm</div>
    <div class="title title-sugar">Sugar</div>
    <div class="veil"></div>
    <div class="product-photo" role="img" aria-label="Photo of round palm sugar pieces piled together"></div>
    <p class="story-en">This is extracted from dense Palmyra palm trees flowers, it is from mother nature.<br>This is 100% naturally derived food.</p>
    <p class="story-jp">メコンデルタの大自然に囲まれ生える<br>オウギヤシの花房から抽出した、100%自然由来食品です。</p>
    <div class="palm-photo" role="img" aria-label="Photo of tall palm trees against the sky"></div>
  </div>
</div>
</body>
</html>
```